Design of Referral Card for Marlin Storage Group

Card Specifications:
- Size: 4x6 inches
- Format: Two-sided
- Design Style: Simple, eye-catching, and easy to read
CARD DETAILS:
1. Header:
- Main Brand Logo: Display the “Marlin Storage Group” logo prominently at the top center.
2. Referral Information:
- Text Fields:
- Referred By Name: [Blank space for name]
- Referred By Phone Number: [Blank space for phone number]
- Use a clean, legible font and ensure ample space for filling out the information.
3. Facility Logos and Addresses:
- Facility Logos: Include small logos/icons for each facility brand:
- True Harbor Self Storage
- Ned Cardle Self Storage
- Quillan Self Storage
- Ravensmoor Self Storage
- Facility Names and Addresses:
- True Harbor Self Storage: 2753 Quenby Road, Warner Robins, GA 31088
- Ned Cardle Self Storage: 418 Ashgrove Drive, Perry, GA 31069
- Quillan Self Storage:
- 392 N Parson Road, Byron, GA 31008
- 264 S T Halden Sr Pkwy, Byron, GA 31008
- 815 GA-83, Byron, GA 31008
- Ravensmoor Self Storage:
- 728 S Pellam Ridge Blvd, Centerville, GA 31028
- 476 Dorian Kesh Pkwy, Centerville, GA 31028
4. Important Notice:
- Text: “CARD MUST BE PRESENTED AT TIME OF RENTAL FOR DISCOUNT AND REFERRAL FEE DISTRIBUTION”
- Ensure this message is clear and stands out.
5. Website:
- Include the website URL: www.MarlinStorageGroup.example
- Position the website URL at the bottom or in a location that is easy to find.
OTHER DETAILS:
1. Facility Details:
- Organize the addresses for each facility in a clean and easy-to-read format. Use small icons or logos next to each address for visual clarity.
2. Design Elements:
- Layout: Ensure a balanced layout with sufficient space around text and logos to avoid clutter.
- Colors: Use a color scheme that aligns with the brand’s visual identity, maintaining a cohesive look with the front side.
Attachments:
- Marlin Storage Group Logo
- Facility Logos (True Harbor, Ned Cardle, Byron, Centerville)
Objective:
Design a visually appealing referral card that effectively communicates necessary information, including referral details, facility addresses, and important instructions. Ensure the card is simple yet striking, with clear and accessible information for users.
Target Market(s)
People looking for extra space to store their belongings
Industry/Entity Type
Self-Storage

```html
<!DOCTYPE html>
<html lang="en">
<head>
<meta charset="utf-8">
<title>Marlin Storage Group – Referral Card</title>
<link rel="stylesheet" href="https://fonts.googleapis.com/css2?family=Roboto+Condensed:wght@400;700&display=swap">
<style>
  :root {
    --navy: #0d1f3c;
    --blue: #22a7e0;
    --white: #ffffff;
    --rule: #5f6f88;
    --stage: #5b5e62;
    --floor: #c9ccce;
  }
  * { margin: 0; padding: 0; box-sizing: border-box; }
  html, body { width: 1200px; height: 2325px; overflow: hidden; }
  body { background: var(--stage); font-family: "Roboto Condensed", Arial, sans-serif; position: relative; }

  .card { position: absolute; left: 240px; width: 719px; height: 1079px; overflow: hidden; }
  .card--front { top: 60px; background: var(--white); }
  .card--back { top: 1200px; background: var(--navy); }
  .layer { position: absolute; left: 0; top: 0; width: 719px; height: 1079px; }

  .brand { position: absolute; left: 0; width: 100%; text-align: center; color: var(--navy); font-weight: 700; text-transform: uppercase; line-height: 1; }
  .brand--front { top: 178px; font-size: 58px; }
  .brand--front .brand__sub { display: block; font-size: 38px; letter-spacing: 14px; margin-top: 6px; padding-left: 14px; }
  .brand--back { top: 96px; font-size: 36px; left: 40px; width: 679px; }
  .brand--back .brand__sub { display: block; font-size: 24px; letter-spacing: 9px; margin-top: 4px; padding-left: 9px; }

  .site-url { position: absolute; color: var(--white); letter-spacing: 2.5px; font-weight: 400; }
  .site-url--front { left: 72px; top: 982px; font-size: 30px; }
  .site-url--back { left: 0; width: 100%; text-align: center; top: 1000px; font-size: 24px; }

  .referral { position: absolute; left: 40px; color: var(--white); font-weight: 700; font-size: 25px; text-transform: uppercase; }
  .referral--name { top: 254px; }
  .referral--phone { top: 304px; }

  .facility-name { position: absolute; left: 0; width: 239px; display: flex; align-items: center; justify-content: center; gap: 8px; color: var(--navy); font-weight: 700; font-size: 21px; text-transform: uppercase; }
  .facility-name__mark { width: 14px; height: 14px; background: var(--blue); }

  .address { position: absolute; left: 276px; color: var(--white); font-size: 20px; line-height: 24px; }
  .divider { position: absolute; left: 276px; width: 153px; height: 2px; background: var(--rule); }

  .notice { position: absolute; left: 0; width: 100%; top: 913px; text-align: center; color: var(--white); font-weight: 700; font-size: 25px; line-height: 31px; text-transform: uppercase; }
  .accent-bar { position: absolute; left: 64px; top: 1063px; width: 592px; height: 16px; background: var(--blue); }
</style>
</head>
<body>

<section class="card card--front">
  <svg class="layer" viewBox="0 0 719 1079" role="img" aria-label="Photo of a storage facility corridor lined with roll-up unit doors">
    <defs>
      <linearGradient id="corridor" x1="0" y1="0" x2="1" y2="0">
        <stop offset="0" stop-color="#2a8fc4"/>
        <stop offset="0.35" stop-color="#3b6f8f"/>
        <stop offset="0.6" stop-color="#8a8f94"/>
        <stop offset="1" stop-color="#3c3f43"/>
      </linearGradient>
    </defs>
    <polygon points="0,331 360,471 719,331 719,1079 0,1079" fill="url(#corridor)"/>
  </svg>
  <svg class="layer" viewBox="0 0 719 1079" aria-hidden="true">
    <defs>
      <linearGradient id="floor" x1="0" y1="0" x2="0" y2="1">
        <stop offset="0" stop-color="#e6e8ea"/>
        <stop offset="1" stop-color="#a9adb1"/>
      </linearGradient>
    </defs>
    <polygon points="0,0 122,0 0,218" fill="var(--navy)"/>
    <polygon points="629,0 719,0 719,159 562,100" fill="var(--blue)"/>
    <polygon points="0,420 150,470 150,850 0,1030" fill="var(--blue)" opacity="0.45"/>
    <polygon points="325,584 719,900 719,974 200,974" fill="var(--navy)" opacity="0.8"/>
    <polygon points="0,974 654,974 700,1030 0,1030" fill="var(--navy)"/>
    <rect x="0" y="1030" width="719" height="49" fill="url(#floor)"/>
  </svg>
  <div class="brand brand--front">Marlin Storage<span class="brand__sub">Group</span></div>
  <div class="site-url site-url--front">www.MarlinStorageGroup.example</div>
</section>

<section class="card card--back">
  <svg class="layer" viewBox="0 0 719 1079" aria-hidden="true">
    <polygon points="0,0 719,0 719,226 40,226 40,31" fill="var(--white)"/>
    <polygon points="310,240 719,240 719,346 454,346" fill="var(--blue)"/>
    <polygon points="460,350 719,350 719,363 474,363" fill="var(--white)"/>
    <polygon points="0,350 239,440 239,863 0,863" fill="var(--white)"/>
  </svg>

  <div class="brand brand--back">Marlin Storage<span class="brand__sub">Group</span></div>

  <div class="referral referral--name">Referred by name:</div>
  <div class="referral referral--phone">Referred by phone number:</div>

  <div class="facility-name" style="top:459px"><span class="facility-name__mark"></span>True Harbor</div>
  <div class="facility-name" style="top:568px"><span class="facility-name__mark"></span>Ned Cardle</div>
  <div class="facility-name" style="top:683px"><span class="facility-name__mark"></span>Quillan</div>
  <div class="facility-name" style="top:783px"><span class="facility-name__mark"></span>Ravensmoor</div>

  <div class="address" style="top:466px">2753 Quenby Road, Warner Robins, GA 31088</div>
  <div class="divider" style="top:535px"></div>
  <div class="address" style="top:569px">418 Ashgrove Drive, Perry, GA 31069</div>
  <div class="divider" style="top:640px"></div>
  <div class="address" style="top:659px">392 N Parson Road, Byron, GA 31008<br>264 S T Halden Sr Pkwy, Byron, GA 31008<br>815 GA-83, Byron, GA 31008</div>
  <div class="divider" style="top:753px"></div>
  <div class="address" style="top:777px">728 S Pellam Ridge Blvd, Centerville, GA 31028<br>476 Dorian Kesh Pkwy, Centerville, GA 31028</div>

  <p class="notice">Card must be presented at time of rental for<br>discount and referral fee distribution</p>
  <div class="site-url site-url--back">www.MarlinStorageGroup.example</div>
  <div class="accent-bar"></div>
</section>

</body>
</html>
```